Design a New Site for a very cool Watch

We have the overall design element of the website and the banners in the PSD file. We need someone to finish our design in PSD and than convert to HTML. We have included the instructions, PSD file, images and all text.

We currently use Hubspot to host and make changes to our site. The entire design aspect is complete so all we need is some minor changes and additions within the photoshop design and than the coding into HTML.

Please only sign up if you understand photoshop and HTML conversion

Here is the DropBox link to the files
https://files.quorvel-share.net/s/pm4kx82lwq7dtne/Belthor%20Site.zip
Updates

We have the basic design concept in Photoshop.  We just need someone who can complete some changes, make some additions and convert to HTML

Target Market(s)

Watch Buyers

Requirements
Must have
• Must look like a professional luxury brand

Our brand colors are very basic with Black, White and Grey can be used

```html
<!DOCTYPE html>
<html lang="en">
<head>
<meta charset="utf-8">
<title>Belthor &amp; Co.</title>
<link rel="stylesheet" href="https://fonts.googleapis.com/css2?family=Marcellus&family=Roboto+Condensed:wght@700&family=Open+Sans:wght@400&display=swap">
<style>
:root{
  --ink:#111;
  --paper:#f1f0ef;
  --nav-text:#555;
  --pink:#d9228a;
  --pink-dark:#bd1f7a;
  --blue:#2aa9dc;
  --blue-text:#2ea3d3;
  --lime:#bcd400;
  --lime-dark:#a2bb00;
  --olive:#99ab00;
  --teal:#2f8fb3;
  --white:#fff;
}
*{margin:0;padding:0;box-sizing:border-box}
html,body{width:1200px;height:691px;overflow:hidden;background:var(--ink)}
.page{position:relative;width:1200px;height:691px;overflow:hidden;background:var(--ink)}
.sidebar{position:absolute;left:0;top:0;width:286px;height:691px;background:var(--paper)}
.brand{position:absolute;left:0;top:188px;width:286px;text-align:center;font-family:"Marcellus",serif;font-size:22px;color:var(--ink);letter-spacing:1px;text-transform:uppercase}
.main-nav{position:absolute;left:26px;top:247px;width:260px;list-style:none}
.main-nav li{height:33px;line-height:34px;margin-bottom:5.6px;padding-left:12px;font-family:"Marcellus",serif;font-size:16px;color:var(--nav-text);text-transform:uppercase}
.main-nav li.is-current{background:var(--ink);color:var(--white)}
.share{position:absolute;left:37px;top:656px;display:flex;align-items:center;gap:6px;font-family:"Marcellus",serif;font-size:16px;color:#444}
.share-label{margin-right:8px}
.share-dot{width:17px;height:17px;border-radius:50%;background:#555}
.tile{position:absolute;overflow:hidden}
.photo{position:absolute}
.heading{font-family:"Roboto Condensed",sans-serif;font-weight:700;text-transform:uppercase;letter-spacing:-1px}
.copy{font-family:"Open Sans",sans-serif;font-size:11px;line-height:14.5px;color:var(--white)}
.story{left:290px;top:0;width:303px;height:213px;background:var(--ink)}
.story-panel{position:absolute;left:0;top:0;width:303px;height:183px;background:linear-gradient(180deg,var(--pink),var(--pink-dark))}
.story .heading{position:absolute;left:2px;top:-4px;font-size:54px;line-height:45px;color:var(--white)}
.story .copy{position:absolute;left:168px;top:66px;width:126px}
.cta{position:absolute;display:flex;align-items:center;font-family:"Roboto Condensed",sans-serif;font-weight:700;font-size:21px;text-transform:uppercase}
.story .cta{left:169px;top:183px;width:134px;height:30px;background:var(--white);color:var(--pink-dark);padding-left:10px}
.cta svg{margin-left:auto;margin-right:8px}
.register{left:897px;top:213px;width:303px;height:214px;background:var(--ink)}
.register-panel{position:absolute;left:0;top:0;width:303px;height:182px;background:var(--blue)}
.register .heading{position:absolute;right:0;top:0;color:var(--white);text-align:right}
.register .line-sm{display:block;font-size:50px;line-height:44px}
.register .line-lg{display:block;font-size:68px;line-height:54px}
.register .cta{left:10px;top:185px;height:26px;color:var(--blue-text);font-size:21px}
.register .cta svg{margin-left:10px}
.repair{left:593px;top:427px;width:304px;height:212px;background:var(--white)}
.repair-panel{position:absolute;left:0;top:0;width:304px;height:182px;background:linear-gradient(180deg,var(--lime),var(--lime-dark))}
.repair .heading{position:absolute;left:4px;top:3px;color:var(--ink)}
.repair .line-lg{display:block;font-size:40px;line-height:33px}
.repair .line-md{display:block;font-size:31px;line-height:26px}
.repair .copy{position:absolute;left:4px;top:92px;width:236px}
.repair .cta{left:7px;top:184px;height:28px;color:var(--olive)}
.news{left:897px;top:427px;width:303px;height:212px;background:linear-gradient(135deg,#f3f2ee,#dedcd6)}
.news .heading{position:absolute;line-height:1}
.news-register{left:8px;top:69px;font-size:33px;color:var(--olive)}
.news-find{left:8px;top:98px;font-size:26px;color:var(--ink)}
.news-about{left:8px;top:116px;font-size:33px;color:var(--teal)}
.news-watch{left:127px;top:64px;font-size:58px;color:var(--pink-dark)}
.news-collection{left:179px;top:118px;font-size:26px;color:var(--ink)}
.footer{position:absolute;left:290px;top:639px;width:910px;height:52px;background:var(--ink);font-family:"Marcellus",serif;font-size:11px;color:var(--white);text-transform:uppercase}
.footer-links{list-style:none}
.footer-links li{position:absolute;top:21px}
.copyright{position:absolute;right:19px;top:21px}
</style>
</head>
<body>
<div class="page">
  <aside class="sidebar">
    <div class="brand">Belthor &amp; Co.</div>
    <ul class="main-nav">
      <li class="is-current">Home</li>
      <li>About Us</li>
      <li>Contact</li>
      <li>Collection</li>
      <li>Lifestyle</li>
      <li>Media</li>
      <li>Shop Now</li>
    </ul>
    <div class="share">
      <span class="share-label">Spread the Word</span>
      <span class="share-dot" aria-label="Social link"></span>
      <span class="share-dot" aria-label="Social link"></span>
      <span class="share-dot" aria-label="Social link"></span>
      <span class="share-dot" aria-label="Social link"></span>
    </div>
  </aside>

  <section class="tile story">
    <div class="story-panel">
      <h2 class="heading">The<br>Veyra<br>Story</h2>
      <p class="copy">Etiam non felis mi. Quisque feugiat, lectus non feugiat consectetur, purus ipsum lobortis nisl, a sollicitudin risus arcu elementum risus. Sed feugiat mollis</p>
    </div>
    <a class="cta">Details
      <svg width="12" height="20" viewBox="0 0 12 20"><path d="M1 1l10 9-10 9" fill="none" stroke="currentColor" stroke-width="1.5"/></svg>
    </a>
  </section>

  <div class="tile photo" style="left:593px;top:0;width:304px;height:213px;background:radial-gradient(circle at 50% 45%,#6a6c78 0%,#2a2b33 25%,#050505 60%)" role="img" aria-label="Cut diamond on black reflective surface"></div>
  <div class="tile photo" style="left:897px;top:0;width:303px;height:213px;background:linear-gradient(135deg,#1a1a1a 0%,#3b2020 30%,#e62219 55%,#d81c14 80%,#2a2a2a 100%)" role="img" aria-label="Square watch with red dial and red strap"></div>
  <div class="tile photo" style="left:290px;top:213px;width:303px;height:214px;background:radial-gradient(ellipse at 55% 55%,#5d5d5d 0%,#262626 35%,#050505 70%)" role="img" aria-label="Scattered crystals on black"></div>
  <div class="tile photo" style="left:593px;top:213px;width:304px;height:214px;background:linear-gradient(135deg,#1c1c1c 0%,#8a8885 35%,#e4e2e0 60%,#bdbab6 85%,#5a5856 100%)" role="img" aria-label="Square watch with white dial and white strap"></div>

  <section class="tile register">
    <div class="register-panel">
      <h2 class="heading"><span class="line-sm">Register</span><span class="line-lg">Your</span><span class="line-lg">Watch</span></h2>
    </div>
    <a class="cta">Register Now
      <svg width="12" height="20" viewBox="0 0 12 20"><path d="M1 1l10 9-10 9" fill="none" stroke="currentColor" stroke-width="1.5"/></svg>
    </a>
  </section>

  <div class="tile photo" style="left:290px;top:427px;width:303px;height:212px;background:linear-gradient(135deg,#f2f2f2 0%,#8c8c94 20%,#1d1d2b 45%,#2c2c40 75%,#6b6b7a 100%)" role="img" aria-label="Square watch with dark dial and floating crystals"></div>

  <section class="tile repair">
    <div class="repair-panel">
      <h2 class="heading"><span class="line-lg">Repair</span><span class="line-md">Maintainance</span><span class="line-md">&amp; Warranty Info</span></h2>
      <p class="copy">Etiam non felis mi. Quisque feugiat, lectus non feugiat consectetur, purus ipsum lobortis nisl, a sollicitudin risus arcu elementum risus. Sed feugiat mollis</p>
    </div>
    <a class="cta">Click Here</a>
  </section>

  <section class="tile news">
    <span class="heading news-register">Register</span>
    <span class="heading news-find">To Find Out</span>
    <span class="heading news-about">About New</span>
    <span class="heading news-watch">Watch</span>
    <span class="heading news-collection">Collcetion</span>
  </section>

  <footer class="footer">
    <ul class="footer-links">
      <li style="left:18px">Contact Us</li>
      <li style="left:118px">Terms of Services</li>
      <li style="left:253px">Refund Policy</li>
      <li style="left:371px">Privacy Policy</li>
    </ul>
    <span class="copyright">© Copyright 2013. All Rights Reserved.</span>
  </footer>
</div>
</body>
</html>
```